Family Photography A5 Invitation to prospective clients

A restaurant will give me public space at their entrance to promote my family photography. I need an A5 vertical layout design for a card to 'invite' potential clients to call me. I am a portrait photographer in Perth, Western Australia. The A5 cards will be taken away by potential clients. They are encouraged to call the studio to register their interest with a view to having a very beautiful family portrait in the studio or on location. This will save the family $250 because the fee will be waived. Locations for photography can include a sunset at the famous Wendham Beach or parks in the Western Suburbs of Perth. Prefer Indesign work file so that I can change images for reprints later. Will be happy to give extra ongoing work to the successful designer on future projects. I'm happy to take positional images in the design and change them later.

Target Market(s)

Women mainly in the 30 to 45 years age group

Industry/Entity Type

Restaurant

Font styles to use
Sans Serif

Requirements
Must have
• Call to action and lively design that gets attention. Prefer to have some similarity with style of web site marlowimaging.com.au
Nice to have
• Prefer not to have the look of fake 'competitions' but rather an invitation to have a beautiful experience and with the opportunity to purchase a beautiful piece of art that celebrates their family. See word doc for previous idea with 'win a portrait...' Some of the words might be useful. More here... Brent Marlow’s photography hangs on thousands of walls in Perth’s homes. His family portraits are not so much photographs as works of art, each one perfect in its own way, a unique interplay of light, shade, colour and composition. They’re the ones that make people say more than just, ‘Oh, nice’. They make people linger and say, ‘Wow, amazing!’.
Should not have
• Avoid too much emphasis on cost. I am not competing on cost, but rather trying to inspire the potential client. See word doc for previous idea with 'win a portrait...' Some of the words might be useful.

```html
<!DOCTYPE html>
<html lang="en">
<head>
<meta charset="utf-8">
<title>Marlow Imaging – Portrait Session Invitation</title>
<link rel="stylesheet" href="https://fonts.googleapis.com/css2?family=Open+Sans:wght@400;600;700&family=Great+Vibes&display=swap">
<style>
  :root {
    --green: #4b9a2c;
    --green-dark: #2f7a1c;
    --ink: #3a3a3a;
    --paper: #ffffff;
    --sea-top: #f2e3c4;
    --sea-mid: #7fb9c4;
    --sea-deep: #3f8fa3;
    --band: #8ccad0;
    --band-deep: #6fb6bf;
  }
  * { margin: 0; padding: 0; box-sizing: border-box; }
  html, body { width: 847px; height: 1200px; overflow: hidden; background: var(--paper); }
  .card {
    position: relative; width: 847px; height: 1200px; background: var(--paper);
    font-family: "Open Sans", Arial, sans-serif; color: var(--ink);
  }
  .brand {
    position: absolute; left: 52px; top: 40px; display: flex; align-items: center; gap: 16px;
  }
  .brand-dot { width: 22px; height: 22px; border-radius: 50%; background: var(--ink); }
  .brand-name { font-size: 34px; font-weight: 600; color: var(--ink); letter-spacing: 1px; }
  .portrait-photo {
    position: absolute; left: 505px; top: 42px; width: 140px; height: 140px; border-radius: 50%;
    background: radial-gradient(circle at 50% 40%, #cfd8dc, #8ea4ad 70%, #6d8690);
    border: 4px solid #e6e6e6;
  }
  .call-box {
    position: absolute; left: 668px; top: 44px; width: 148px; height: 136px;
    background: var(--green); color: #fff; text-align: center; padding-top: 14px;
  }
  .call-box .small { font-size: 30px; line-height: 1; }
  .call-box .big { font-size: 40px; line-height: 1.1; }
  .call-box .phone { font-size: 20px; font-weight: 700; margin-top: 6px; }
  .headline {
    position: absolute; top: 236px; left: 0; width: 100%; text-align: center;
    font-size: 27px; font-weight: 700; color: var(--green);
  }
  .letter {
    position: absolute; top: 286px; left: 38px; width: 771px;
    column-count: 2; column-gap: 34px;
    font-size: 13.4px; line-height: 1.42; text-align: left;
  }
  .letter p { margin-bottom: 10px; }
  .letter .price { color: var(--green); font-weight: 600; }
  .letter .sign { text-align: right; color: var(--green); font-weight: 700; font-size: 20px; margin-top: 4px; }
  .beach-photo {
    position: absolute; top: 640px; left: 0; width: 847px; height: 430px;
    background: linear-gradient(180deg, #cfe0ea 0%, #f4e6c8 32%, #e9c898 46%, var(--sea-mid) 62%, var(--sea-deep) 82%, var(--band) 100%);
  }
  .footer {
    position: absolute; top: 1070px; left: 0; width: 847px; height: 130px;
    background: linear-gradient(180deg, var(--band) 0%, var(--band-deep) 100%);
    text-align: center; color: #fff;
  }
  .footer .invite { font-size: 21px; padding-top: 6px; }
  .footer .call { font-size: 30px; font-weight: 700; color: var(--green-dark); margin-top: 2px; }
  .footer .address { font-size: 13px; color: #1f4d3a; margin-top: 4px; }
  .footer .web { font-size: 13px; color: #1f4d3a; }
</style>
</head>
<body>
<main class="card">
  <header>
    <div class="brand">
      <span class="brand-dot"></span>
      <span class="brand-name">Marlow Imaging</span>
    </div>
    <div class="portrait-photo" role="img" aria-label="Photograph of the photographer riding a bicycle, in a circular frame"></div>
    <div class="call-box">
      <div class="small">Call me</div>
      <div class="big">NOW</div>
      <div class="phone">0412 555 018</div>
    </div>
  </header>

  <h1 class="headline">Free portrait session valued at $250</h1>

  <section class="letter">
    <p>Well, well, well... Who’d have imagined that your visit to Corsetti Restaurant in North Wendham would win you a free portrait session (valued at <span class="price">$250</span>) with a renowned Western European photographer?</p>
    <p>Unless you’re one of those charmed people who seem to win everything they enter, this is probably a bolt from the blue... but yes, it’s true. You’re a WINNER!</p>
    <p>This is your opportunity to possess the most beautiful photographic art of yourself and your loved ones. We’re looking forward to giving you the experience of a photography session you’ll never forget.</p>
    <p>You’ll be asked to imagine your perfect backdrop. Will it be the ocean? A park full of beautiful flowers and greenery? Or perhaps you’d prefer a creative black and white studio session at our Westhaven studio? The choice is yours.</p>
    <p>After your session, we’ll arrange a cinema experience to highlight the many ways of presenting your beautiful images. We guarantee that your images will reflect personality, humour and love. Like so many of our clients, you’ll probably return in future years because our work really does keep on giving.</p>
    <p>See yourself in a new light. All you need do now is pick up the phone and call Brent to book your session. How easy is that?</p>
    <p>Heartiest congratulations and best wishes,</p>
    <p class="sign">Brent Marlow</p>
  </section>

  <div class="beach-photo" role="img" aria-label="Sunset photograph of Wendham Beach with a pavilion, sand and gentle waves"></div>

  <footer class="footer">
    <p class="invite">Book your family photography session today!</p>
    <p class="call">Call us on 0412 555 018</p>
    <p class="address">Office Admin 18 Alder St. Kingsbay 6010. Studio 37 Garnet St. Westhaven 6159</p>
    <p class="web">www.marlowimaging.com.au</p>
  </footer>
</main>
</body>
</html>
```